Business Card Design

We need a business card design for a Dry cleaners in Brisbane, Australia. We are trying to promote a fresh/clean image consistent with our website. www.finchlanelaundry.com.au

Looking for a professional neat card that's easy to read.

Target Market(s)

Customers looking for a professional, fresh and clean drycleaners.

Industry/Entity Type

Business

Contact Information for Business Card

See our existing business card. The Fax number (07) 3648 2051 to be removed.

Requirements
Must have
• All the details on current business card less the fax number.
Nice to have
• I like white text on coloured background. Blue works well as we are located near the water...

```html
<!DOCTYPE html>
<html lang="en">
<head>
<meta charset="utf-8">
<title>Finch Lane Laundry – Business Card</title>
<link rel="stylesheet" href="https://fonts.googleapis.com/css2?family=Noto+Sans:wght@400;700&display=swap">
<style>
  :root {
    --page: #ffffff;
    --card-deep: #0010d6;
    --card-mid: #1a2ee8;
    --band: #135ae0;
    --band-edge: #2a5ff0;
    --text: #ffffff;
    --glow: rgba(255, 210, 255, 0.9);
  }
  * { margin: 0; padding: 0; box-sizing: border-box; }
  html, body {
    width: 1200px; height: 1000px; overflow: hidden;
    background: var(--page);
    font-family: "Noto Sans", Verdana, sans-serif;
    color: var(--text);
  }
  .card {
    position: absolute; left: 45px; top: 157px;
    width: 1110px; height: 685px; overflow: hidden;
    background:
      radial-gradient(circle at 345px 270px, var(--glow) 0, rgba(220,120,255,0.45) 45px, rgba(120,80,255,0.15) 100px, transparent 150px),
      radial-gradient(circle at 700px 410px, rgba(120,150,255,0.35) 0, rgba(90,110,255,0.12) 110px, transparent 160px),
      radial-gradient(circle at 330px 160px, rgba(80,110,255,0.35) 0, transparent 260px),
      linear-gradient(160deg, var(--card-mid) 0%, var(--card-deep) 60%);
  }
  .card-waves { position: absolute; inset: 0; }
  .wordmark {
    position: absolute; left: 100px; top: 170px;
    display: flex; align-items: center; gap: 18px;
    font-size: 60px; font-weight: 700; letter-spacing: 0.5px;
    color: var(--text); white-space: nowrap;
  }
  .wordmark-dot { width: 34px; height: 34px; border-radius: 50%; background: var(--text); }
  .contact { position: absolute; top: 354px; line-height: 1; }
  .contact-person { left: 92px; }
  .contact-name { font-size: 38px; font-weight: 700; margin-bottom: 12px; }
  .contact-line { font-size: 28px; line-height: 34px; white-space: nowrap; }
  .contact-shop { left: 746px; top: 356px; }
  .contact-shop .contact-line { font-size: 30px; line-height: 40px; }
  .locations {
    position: absolute; left: 0; right: 0; top: 596px;
    display: flex; justify-content: center; gap: 50px;
    font-size: 44px; line-height: 1; white-space: nowrap;
  }
</style>
</head>
<body>
  <main class="card">
    <svg class="card-waves" width="1110" height="685" viewBox="0 0 1110 685" aria-hidden="true">
      <circle cx="700" cy="410" r="260" fill="none" stroke="rgba(140,160,255,0.25)" stroke-width="3"/>
      <circle cx="650" cy="370" r="75" fill="rgba(150,170,255,0.18)"/>
      <circle cx="695" cy="390" r="30" fill="rgba(160,190,255,0.35)"/>
      <circle cx="510" cy="325" r="22" fill="rgba(160,170,255,0.25)"/>
      <path d="M0 545 C 250 470, 520 500, 760 555 C 900 585, 1030 540, 1110 485 L1110 505 C 1030 560, 900 600, 760 570 C 520 520, 250 495, 0 560 Z" fill="var(--band-edge)" opacity="0.5"/>
      <path d="M0 556 C 250 490, 520 520, 760 570 C 900 598, 1030 555, 1110 500 L1110 685 L0 685 Z" fill="var(--band)"/>
    </svg>

    <div class="wordmark"><span class="wordmark-dot"></span>Finch Lane Laundry</div>

    <section class="contact contact-person">
      <p class="contact-name">Jordan Ellery</p>
      <p class="contact-line">M: 0412 558 304</p>
      <p class="contact-line">E: jordan@finchlanelaundry.com.au</p>
    </section>

    <section class="contact contact-shop">
      <p class="contact-line">27 Marlow St</p>
      <p class="contact-line">Harbourne Qld 4190</p>
      <p class="contact-line">P: (07) 3521 4762</p>
    </section>

    <nav class="locations">
      <span>Harbourne</span><span>|</span><span>Kestrel Bay</span><span>|</span><span>Marlin Pt</span>
    </nav>
  </main>
</body>
</html>
```